Food packaging label design

The product name Crisplets, a thin, crispy, and delicious biscuit/cookie made from simple, all natural ingredients. Its name comes from the fact that it looks and tastes a lot like a biscotti cookie, but thinly sliced and much crispier and more delicious than a biscotti. There are currently two flavors: Pure Harvest, and Maple Orchard.

I am looking for a fresh, eye catchy design to go on the label for a rice paper stand up pouch (pouch sample attached). Label size are as follows:

4 oz bag - Width X Height
top: 4.5" x 3.5" bottom: 4.5" x 1.5"

12 oz bag
top: 6.5" x 5.5" bottom: 6.5" x 1.5"

I would like for the top portion of the packaging to include:

Crisplets name
Tag line " a thinner, crispier, and more delicious cousin to the biscotti"
simple and natural ingredients

bottom to include:
net weight
ingredients: wheat flour, eggs, sugar, almonds

Attached is a copy of something I created in powerpoint. you can recreate this using graphic designer software per label specs and improve on it or supprise me with something totally awesome. The key is that it that the colors and design needs to pop or contrast against the white rice paper bag and design needs to be eye catchy, fun and whimsical.

Please refer to link below for best practices for creating artwork for labels to ensure correct format for printing.
http://www.printwellmark.example/label-articles/best-practices-designing-custom-labels/

Good luck!
Updates

Target Market(s)

educated, health conscious consumers such as customers who shops at green basket, brewhollow, market pennys

Industry/Entity Type

Graphic Designer

Requirements
Should not have
• busy or clutter design

```html
<!DOCTYPE html>
<html lang="en">
<head>
<meta charset="utf-8">
<title>Crisplets pouch labels</title>
<link rel="stylesheet" href="https://fonts.googleapis.com/css2?family=Poppins:wght@500;600;700&family=Roboto:wght@400;500;700&family=Roboto+Condensed:wght@400;700&family=Rochester&display=swap">
<style>
  :root {
    --paper: #f4efe5;
    --white: #ffffff;
    --ink: #2a1c14;
    --maroon: #7b1e1e;
    --almond-top: #e0b070;
    --almond-bottom: #c98b45;
    --rule: #2a1c14;
  }
  * { box-sizing: border-box; margin: 0; padding: 0; }
  html, body { width: 1200px; height: 462px; overflow: hidden; background: var(--white); }
  .sheet { position: relative; width: 1200px; height: 462px; }
  .panel { position: absolute; top: 0; width: 298px; height: 462px; background: var(--paper); overflow: hidden; color: var(--ink); }
  .panel--1 { left: 0; }
  .panel--2 { left: 301px; }
  .panel--3 { left: 602px; }
  .panel--4 { left: 903px; }

  /* front panel */
  .almond-band { position: absolute; left: 0; top: 0; width: 100%; height: 22px;
    background: linear-gradient(var(--almond-top), var(--almond-bottom)); }
  .product-name { position: absolute; left: 0; top: 108px; width: 100%; text-align: center;
    font-family: "Poppins", sans-serif; font-weight: 700; font-size: 46px; letter-spacing: 1px; color: var(--ink); }
  .flavor-row { position: absolute; left: 8px; top: 190px; right: 6px; display: flex; align-items: center; }
  .flavor { text-align: center; padding-right: 7px; border-right: 1.5px solid var(--ink); white-space: nowrap; }
  .flavor__script { font-family: "Rochester", cursive; font-size: 19px; line-height: 1; }
  .flavor__caps { font-family: "Poppins", sans-serif; font-weight: 500; font-size: 11px; letter-spacing: .5px; line-height: 1.2; }
  .tagline { padding-left: 7px; font-family: "Poppins", sans-serif; font-weight: 500; font-size: 11px; line-height: 1.4; color: var(--maroon); white-space: nowrap; }
  .tagline b { font-weight: 500; color: var(--ink); }
  .window { position: absolute; left: 0; top: 222px; width: 100%; height: 133px; background: var(--white); }
  .claim { position: absolute; left: 0; top: 372px; width: 100%; text-align: center;
    font-family: "Rochester", cursive; font-size: 30px; color: var(--ink); white-space: nowrap; }
  .ingredients { position: absolute; left: 10px; top: 424px; font-family: "Poppins", sans-serif; font-weight: 500; font-size: 8.2px; color: var(--maroon); white-space: nowrap; }
  .ingredients span { color: var(--ink); }
  .net-weight { position: absolute; right: 8px; top: 448px; font-family: "Roboto", sans-serif; font-size: 7.5px; }

  /* back panel */
  .story { position: absolute; left: 13px; top: 16px; width: 141px; height: 327px; border: 1.5px solid var(--rule);
    padding: 5px 5px; font-family: "Roboto", sans-serif; font-size: 8.8px; line-height: 13.6px; overflow: hidden; }
  .facts { position: absolute; left: 159px; top: 16px; width: 132px; height: 272px; border: 1.5px solid var(--rule);
    padding: 3px 4px; font-family: "Roboto Condensed", sans-serif; font-size: 6px; line-height: 1.2; overflow: hidden; }
  .facts__title { font-family: "Roboto", sans-serif; font-weight: 700; font-size: 16px; line-height: 1; white-space: nowrap; }
  .facts__head { font-weight: 700; font-size: 7px; line-height: 1.15; border-bottom: 4px solid var(--rule); padding-bottom: 2px; }
  .facts__row { display: flex; justify-content: space-between; border-bottom: .6px solid var(--rule); padding: .8px 0; white-space: nowrap; }
  .facts__row--sub { padding-left: 8px; }
  .facts__row--thick { border-bottom: 3px solid var(--rule); }
  .facts__row b { font-weight: 700; }
  .facts__note { font-size: 5.2px; line-height: 1.15; padding-top: 2px; }
  .facts__grid { display: grid; grid-template-columns: 1fr 30px 24px 24px; font-size: 5px; line-height: 1.1; margin-top: 2px; border-top: .6px solid var(--rule); white-space: nowrap; }
  .facts__grid span:nth-child(4n+2), .facts__grid span:nth-child(4n+3), .facts__grid span:nth-child(4n) { text-align: right; }
  .facts__cal { font-size: 5px; line-height: 1.15; margin-top: 2px; border-top: .6px solid var(--rule); }
  .allergens { position: absolute; left: 159px; top: 302px; width: 132px; text-align: center; font-family: "Roboto", sans-serif; font-size: 10px; line-height: 1.35; white-space: nowrap; }
  .allergens b { display: block; font-weight: 700; font-size: 10.5px; }
  .upc-box { position: absolute; left: 166px; top: 341px; width: 125px; height: 80px; border: 1.5px solid var(--rule);
    display: flex; align-items: center; justify-content: center; text-align: center; font-family: "Roboto", sans-serif; font-weight: 700; font-size: 12px; line-height: 1.3; }
  .maker { position: absolute; left: 4px; top: 354px; width: 158px; text-align: center; font-family: "Roboto", sans-serif; font-size: 11.5px; line-height: 1.3; white-space: nowrap; }
  .maker b { font-weight: 700; }
  .orders { position: absolute; left: 4px; top: 427px; width: 200px; text-align: left; font-family: "Poppins", sans-serif; white-space: nowrap; }
  .orders__label { font-size: 5.6px; font-weight: 600; }
  .orders__site { font-size: 13px; font-weight: 700; line-height: 1.2; }
</style>
</head>
<body>
<main class="sheet">

  <section class="panel panel--1" aria-label="Maple Orchard front label">
    <div class="almond-band" role="img" aria-label="Row of illustrated almonds along the top edge"></div>
    <h1 class="product-name">CRISPLETS</h1>
    <div class="flavor-row">
      <div class="flavor"><div class="flavor__script">Maple</div><div class="flavor__caps">ORCHARD</div></div>
      <p class="tagline"><b>A THINNER</b>, CRISPIER, AND MORE<br>DELICIOUS COUSIN TO THE BISCOTTI</p>
    </div>
    <div class="window"></div>
    <p class="claim">Simple and Natural</p>
    <p class="ingredients">INGREDIENTS: <span>WHEAT FLOUR, EGGS, SUGAR, ALMONDS, CRANBERRY</span></p>
    <p class="net-weight">NET WT. 2 OZ.</p>
  </section>

  <section class="panel panel--2" aria-label="Maple Orchard back label">
    <p class="story">Crisplets is a thin, crispy, and delicious biscuit/cookie made from simple and all natural ingredients. Pure Harvest flavor is made from just 4 simple ingredients: egg whites, all purpose flour, sugar, and almonds. The name Crisplets comes from its twice cooked process and then thinly sliced to perfection. The crispy, nutty and delicious flavor resemble that of a biscotti, but without the guilt. In fact, except for naturally healthy omega 3 fat from almonds, Crisplets is made without any fat at all. It is an ideal snack for the health conscious snacker. Go ahead, give it a try... there's a good chance you will be hooked!!!</p>
    <div class="facts">
      <div class="facts__title">Nutrition Facts</div>
      <div class="facts__head">Serving Size (1 oz) (28g)<br>Serving Per Container 2</div>
      <div class="facts__row"><span>Amount per serving</span></div>
      <div class="facts__row facts__row--thick"><b>Calories 90</b><b>Calories from Fat 25</b></div>
      <div class="facts__row"><span></span><span>% Daily Value*</span></div>
      <div class="facts__row"><b>Total Fat 3g</b><span>5%</span></div>
      <div class="facts__row facts__row--sub"><span>Saturated Fat 0g</span><span>0%</span></div>
      <div class="facts__row facts__row--sub"><span>Trans Fat 0g</span></div>
      <div class="facts__row"><b>Cholesterol 0mg</b><span>0%</span></div>
      <div class="facts__row"><b>Sodium 15mg</b><span>1%</span></div>
      <div class="facts__row"><b>Total Carbohydrate 14g</b><span>5%</span></div>
      <div class="facts__row facts__row--sub"><span>Dietary Fiber 1g</span><span>4%</span></div>
      <div class="facts__row"><b>Sugars 8g</b></div>
      <div class="facts__row facts__row--thick"><b>Proteins 3g</b></div>
      <div class="facts__row"><span>Vitamin A 0%</span><span>• Vitamin C 0%</span></div>
      <div class="facts__row"><span>Calcium 2%</span><span>• Iron 2%</span></div>
      <p class="facts__note">*Percent Daily Values are based on a 2,000 calorie diet. Your daily values may be higher or lower depending on your calorie needs:</p>
      <div class="facts__grid">
        <span></span><span>Calories:</span><span>2,000</span><span>2,500</span>
        <span>Total Fat</span><span>Less than</span><span>65g</span><span>80g</span>
        <span>&nbsp;Saturated Fat</span><span>Less than</span><span>20g</span><span>25g</span>
        <span>Cholesterol</span><span>Less than</span><span>300mg</span><span>300mg</span>
        <span>Sodium</span><span>Less than</span><span>2,400mg</span><span>2,400mg</span>
        <span>Total Carbohydrate</span><span></span><span>300g</span><span>375g</span>
        <span>&nbsp;Dietary Fiber</span><span></span><span>25g</span><span>30g</span>
      </div>
      <p class="facts__cal">Calories per gram:<br>&nbsp;&nbsp;&nbsp;Fat 9 &nbsp;•&nbsp; Carbohydrate 4 &nbsp;•&nbsp; Protein 4</p>
    </div>
    <p class="allergens"><b>CONTAINS:</b>EGG, WHEAT, AND TREE NUT</p>
    <p class="maker"><b>Made in the U.S.A</b><br>Created and Distributed by:<br>Bright Crumb Bakeshop, LLC.<br>Atlanta, Georgia</p>
    <div class="upc-box">Reserved for<br>UPC Label</div>
    <div class="orders"><div class="orders__label">FOR ORDERS AND INQUIRIES, PLEASE VISIT US AT:</div><div class="orders__site">WWW.CRISPLETS.EXAMPLE</div></div>
  </section>

  <section class="panel panel--3" aria-label="Pure Harvest front label">
    <div class="almond-band" role="img" aria-label="Row of illustrated almonds along the top edge"></div>
    <h1 class="product-name">CRISPLETS</h1>
    <div class="flavor-row">
      <div class="flavor"><div class="flavor__caps">PURE</div><div class="flavor__script">Harvest</div></div>
      <p class="tagline"><b>A THINNER</b>, CRISPIER, AND MORE<br>DELICIOUS COUSIN TO THE BISCOTTI</p>
    </div>
    <div class="window"></div>
    <p class="claim">Simple and Natural</p>
    <p class="ingredients">INGREDIENTS: <span>WHEAT FLOUR, EGGS, SUGAR, ALMONDS</span></p>
    <p class="net-weight">NET WT. 2 OZ.</p>
  </section>

  <section class="panel panel--4" aria-label="Pure Harvest back label">
    <p class="story">Crisplets is a thin, crispy, and delicious biscuit/cookie made from simple and all natural ingredients. Pure Harvest flavor is made from just 4 simple ingredients: egg whites, all purpose flour, sugar, and almonds. The name Crisplets comes from its twice cooked process and then thinly sliced to perfection. The crispy, nutty and delicious flavor resemble that of a biscotti, but without the guilt. In fact, except for naturally healthy omega 3 fat from almonds, Crisplets is made without any fat at all. It is an ideal snack for the health conscious snacker. Go ahead, give it a try... there's a good chance you will be hooked!!!</p>
    <div class="facts">
      <div class="facts__title">Nutrition Facts</div>
      <div class="facts__head">Serving Size (1 oz) (25g)<br>Serving Per Container 2</div>
      <div class="facts__row"><span>Amount per serving</span></div>
      <div class="facts__row facts__row--thick"><b>Calories 80</b><b>Calories from Fat 25</b></div>
      <div class="facts__row"><span></span><span>% Daily Value*</span></div>
      <div class="facts__row"><b>Total Fat 2.5g</b><span>5%</span></div>
      <div class="facts__row facts__row--sub"><span>Saturated Fat 0g</span><span>0%</span></div>
      <div class="facts__row facts__row--sub"><span>Trans Fat 0g</span></div>
      <div class="facts__row"><b>Cholesterol 0mg</b><span>0%</span></div>
      <div class="facts__row"><b>Sodium 15mg</b><span>1%</span></div>
      <div class="facts__row"><b>Total Carbohydrate 14g</b><span>5%</span></div>
      <div class="facts__row facts__row--sub"><span>Dietary Fiber 1g</span><span>4%</span></div>
      <div class="facts__row"><b>Sugars 8g</b></div>
      <div class="facts__row facts__row--thick"><b>Proteins 3g</b></div>
      <div class="facts__row"><span>Vitamin A 0%</span><span>• Vitamin C 0%</span></div>
      <div class="facts__row"><span>Calcium 2%</span><span>• Iron 2%</span></div>
      <p class="facts__note">*Percent Daily Values are based on a 2,000 calorie diet. Your daily values may be higher or lower depending on your calorie needs:</p>
      <div class="facts__grid">
        <span></span><span>Calories:</span><span>2,000</span><span>2,500</span>
        <span>Total Fat</span><span>Less than</span><span>65g</span><span>80g</span>
        <span>&nbsp;Saturated Fat</span><span>Less than</span><span>20g</span><span>25g</span>
        <span>Cholesterol</span><span>Less than</span><span>300mg</span><span>300mg</span>
        <span>Sodium</span><span>Less than</span><span>2,400mg</span><span>2,400mg</span>
        <span>Total Carbohydrate</span><span></span><span>300g</span><span>375g</span>
        <span>&nbsp;Dietary Fiber</span><span></span><span>25g</span><span>30g</span>
      </div>
      <p class="facts__cal">Calories per gram:<br>&nbsp;&nbsp;&nbsp;Fat 9 &nbsp;•&nbsp; Carbohydrate 4 &nbsp;•&nbsp; Protein 4</p>
    </div>
    <p class="allergens"><b>CONTAINS:</b>EGG, WHEAT, AND TREE NUT</p>
    <p class="maker"><b>Made in the U.S.A</b><br>Created and Distributed by:<br>Bright Crumb Bakeshop, LLC.<br>Atlanta, Georgia</p>
    <div class="upc-box">Reserved for<br>UPC Label</div>
    <div class="orders"><div class="orders__label">FOR ORDERS AND INQUIRIES, PLEASE VISIT US AT:</div><div class="orders__site">WWW.CRISPLETS.EXAMPLE</div></div>
  </section>

</main>
</body>
</html>
```